Website redesign

PLOBrisk.com is a website that allows real estate investors to search for and find investment grade residential real estate property. The website is up and running, but is in desperate need of a facelift. You can see the existing website at http://www.plobrisk.example. PLO stands for "Real Estate Investor" by the way.
We just finished our design competition for our logo and are now ready to move on to the website design itself!
The industry is real estate, but it is really just focused on the investor market, so we do not cater to the married couple looking to buy their next house. Our clients are business people searching for properties to buy so they can either resell them at a profit or hold them and rent them out.
On the PLOBrisk website, the real estate investor can search for properties using a unique search engine that focuses on the financial aspects of property. Once they find a property, the website allows them to quickly and easily make offers on those properties (investment real estate is sometimes a volume game - you might make offers on 20 houses to secure 1 house).
This website is not about "get rich quick" kind of stuff, so designs with a bunch of dollar signs, or things like that is not what I am looking for.
The design should be tailored to the business person (the real estate investor). Thus, it should be serious, but at the same time have a little edge to it.
We are looking to use modern design elements including:
- A Flat Design - no 3D please
- Large Hero Area – with eye catching imagery and verbiage
- Long scrolling page, but sparse content
- Simple color scheme – bold colors ok, but don’t need all the colors of the rainbow represented
- Larger fonts but with less content. More calls to action
- I would really like to investigate the use of cards for our search results. I’m not convinced this will work, but if we can make it work I think it would be impressive.
IMPORTANT: Out site is a gridkit website, so please ensure that the designs you come up with are capable of being implemented in Quillon GridKit.
If you are a killer designer, there will be more work to come for you as we have a long list of enhancements that will require ongoing UI work.
I will participate heavily in this project, so ask me your questions and I will get back to you very quickly.
Examples of designs that I like:
http://www.vendrapo.example/
http://www.lumestrandstudio.example/
http://www.hobrenta.example
http://www.casqino.example
http://www.pexmoraweb.example/
Your Deliverables:
- 2 Page Concepts:
o Home Page: http://www.plobrisk.example
o Search Page: http://www.plobrisk.example/s/Dallas/flip-houses

```html
<!DOCTYPE html>
<html lang="en">
<head>
<meta charset="utf-8">
<title>PLOBrisk.com – Home</title>
<link rel="stylesheet" href="https://fonts.googleapis.com/css2?family=Raleway:wght@500;600&family=Arimo:wght@400;700&display=swap">
<style>
:root{
  --blue:#22539e;
  --blue-footer:#1f5ea8;
  --orange:#f07d1a;
  --orange-btn:#ff4a0a;
  --ink:#222;
  --text:#333;
  --rule:#cfcfcf;
  --white:#fff;
  --dark:#1b1b1b;
}
*{box-sizing:border-box;margin:0;padding:0}
html,body{width:974px;height:1200px;overflow:hidden}
body{position:relative;background:var(--white);font-family:Arimo,Arial,sans-serif;color:var(--text)}
.abs{position:absolute}

/* header */
.brand{left:84px;top:52px;display:flex;align-items:center;gap:8px}
.brand-dot{width:26px;height:26px;border-radius:50%;background:var(--orange)}
.brand-name{font-family:Raleway,sans-serif;font-weight:600;font-size:26px;color:var(--blue);letter-spacing:-.3px}
.contact-top{top:44px;font-size:11.5px;font-weight:700;color:var(--ink)}
.contact-email{left:623px;top:46px}
.contact-phone{left:763px;display:flex;align-items:center;gap:8px;font-size:13.5px;letter-spacing:.6px}
.nav{top:80px;font-size:13.5px;color:var(--ink)}
.header-rule{left:0;top:108px;width:974px;height:3px;background:var(--rule)}
.nav-active{left:438px;top:107px;width:63px;height:4px;background:var(--orange)}
.nav-caret{left:465px;top:103px;width:0;height:0;border:4px solid transparent;border-bottom-color:var(--orange)}

/* hero */
.hero{left:0;top:111px;width:974px;height:388px;
  background:linear-gradient(180deg,#0a3fd6 0%,#2a66e6 40%,#7ea3e0 62%,#20305a 78%,#1a2f6e 100%)}

/* intro */
.intro-title{left:87px;top:528px;font-family:Raleway,sans-serif;font-weight:500;font-size:28px;color:var(--blue)}
.intro-sub{left:88px;top:570px;font-size:14.5px;color:var(--orange)}
.intro-copy{left:88px;width:800px;font-size:10.4px;line-height:15.4px;color:var(--ink)}

/* search band */
.search-band{left:0;top:738px;width:974px;height:324px;
  background:linear-gradient(180deg,#161616 0%,#2b2d30 55%,#121212 100%)}
.tab{top:786px;height:51px;border:1px solid var(--white);border-bottom:none;border-radius:9px 9px 0 0;
  font-size:17.5px;color:var(--white);padding:13px 0 0 15px}
.tab-active{background:var(--white);color:var(--orange);height:52px;padding-left:8px}
.panel{left:102px;top:836px;width:750px;height:166px;border:1px solid var(--white);border-top:none}
.panel-edge{top:836px;height:1px;background:var(--white)}
.search-lead{left:118px;top:899px;font-size:13.5px;color:var(--white)}
.field-label{top:940px;font-size:13.5px;color:var(--white)}
.select{top:935px;height:27px;background:var(--white);border-radius:2px;font-size:11px;color:#777;padding:7px 8px}
.select svg{position:absolute;right:7px;top:10px}
.search-btn{left:733px;top:934px;width:98px;height:29px;border-radius:15px;background:var(--white);
  border:2px solid #4d86c8;box-shadow:inset 0 0 0 2px #fff,inset 0 0 0 3px #2c68b0;
  font-size:11.5px;color:var(--blue);letter-spacing:.6px;text-align:center;line-height:25px}

/* footer */
.footer{left:0;top:1062px;width:974px;height:138px;background:var(--blue-footer);color:var(--white)}
.f-head{top:1081px;font-size:11.5px;font-weight:700;letter-spacing:.3px;color:var(--white)}
.f-list{list-style:none;font-size:8.8px;line-height:14.6px;color:var(--white)}
.social{display:flex;align-items:center;gap:5px;font-size:8.8px;font-weight:700;color:var(--white)}
.social-mark{width:19px;height:19px;border-radius:3px;background:#4f8bd4}
.f-phone{left:474px;top:1106px;font-size:13.5px;color:var(--white)}
.f-address{left:462px;top:1125px;font-size:8.8px;line-height:16px;color:var(--white)}
.email-input{left:652px;top:1110px;width:178px;height:27px;background:var(--white);border-radius:2px;
  font-size:9.5px;color:#444;padding:8px 10px}
.join-btn{left:838px;top:1112px;width:55px;height:24px;background:var(--orange-btn);border-radius:2px;
  font-size:10.5px;font-weight:700;color:var(--white);text-align:center;line-height:24px}
</style>
</head>
<body>

<header>
  <div class="abs brand"><span class="brand-dot"></span><span class="brand-name">PLOBrisk.com</span></div>
  <div class="abs contact-top contact-email">info@plobrisk.example</div>
  <div class="abs contact-top contact-phone">
    <svg width="22" height="20" viewBox="0 0 22 20" aria-hidden="true"><path d="M2 6c0-3 4-4 9-4s9 1 9 4v2h-4V6H6v2H2z" fill="#111"/><path d="M5 9h12l2 9H3z" fill="#111"/><circle cx="11" cy="13" r="2.5" fill="#fff"/></svg>
    <span>555 0142 7700</span>
  </div>
  <nav>
    <span class="abs nav" style="left:451px">Home</span>
    <span class="abs nav" style="left:530px">Properties</span>
    <span class="abs nav" style="left:635px">About Us</span>
    <span class="abs nav" style="left:735px">Speed Offer</span>
    <span class="abs nav" style="left:850px">Agents</span>
  </nav>
  <div class="abs header-rule"></div>
  <div class="abs nav-active"></div>
  <div class="abs nav-caret"></div>
</header>

<div class="abs hero" role="img" aria-label="Night city skyline of waterfront towers behind a marina full of white yachts under a deep blue sky"></div>

<section>
  <h1 class="abs intro-title">What is PLOBrisk?</h1>
  <p class="abs intro-sub">PLOBrisk was designed by Real Estate Investors for Real Estate Investors.</p>
  <p class="abs intro-copy" style="top:596px">We are a totally unique search engine and workflow system which helps real estate investors quickly find and secure investment grade residential real estate. Unlike our competitors, our service is 100% free to buyers as we only make money through seller paid commissions - in other words, we only make money when you find great properties.</p>
  <p class="abs intro-copy" style="top:658px">dummy text of the printing and typesetting industry. Lorem Ipsum has been the industry's standard dummy text ever since the 1500s, when an unknown printer took a galley of type and scrambled it to make a type specimen book. It has survived not only five centuries, but also the leap into electronic typesetting, remaining essentially unchanged. It was popularised in the 1960s with the release of Ipsum has been the industry's standard dummy text ever since the 1500s,</p>
</section>

<section>
  <div class="abs search-band" role="img" aria-label="Dim photograph of a modern building facade at dusk"></div>
  <div class="abs tab tab-active" style="left:102px;width:268px">I am buying &amp; renting properties</div>
  <div class="abs tab" style="left:390px;width:220px">I am flipping properties</div>
  <div class="abs tab" style="left:632px;width:220px;padding-left:18px">I am an advanced user</div>
  <div class="abs panel"></div>
  <div class="abs panel-edge" style="left:370px;width:20px"></div>
  <div class="abs panel-edge" style="left:610px;width:22px"></div>
  <p class="abs search-lead">Show me properties with the MOST potential equity:</p>
  <span class="abs field-label" style="left:117px">City:</span>
  <div class="abs select" style="left:160px;width:175px">Abbott<svg width="9" height="8" aria-hidden="true"><path d="M0 0h9L4.5 8z" fill="#111"/></svg></div>
  <span class="abs field-label" style="left:366px">Distance from city center</span>
  <div class="abs select" style="left:533px;width:176px">Miles<svg width="9" height="8" aria-hidden="true"><path d="M0 0h9L4.5 8z" fill="#111"/></svg></div>
  <div class="abs search-btn">SEARCH</div>
</section>

<footer>
  <div class="abs footer"></div>
  <h4 class="abs f-head" style="left:85px">Quick Links</h4>
  <ul class="abs f-list" style="left:88px;top:1103px"><li>Home</li><li>Blog</li><li>Products</li><li>About</li><li>Contact</li></ul>
  <h4 class="abs f-head" style="left:222px">Follow Us</h4>
  <div class="abs social" style="left:223px;top:1106px"><span class="social-mark"></span>Chatterbook</div>
  <div class="abs social" style="left:223px;top:1138px"><span class="social-mark"></span>Tweetline</div>
  <h4 class="abs f-head" style="left:354px">Help</h4>
  <ul class="abs f-list" style="left:353px;top:1104px"><li>How it Works?</li><li>FAQs</li><li>Privacy Policy</li><li>Term of Use</li></ul>
  <h4 class="abs f-head" style="left:463px">Contact</h4>
  <div class="abs f-phone">55501-427700</div>
  <div class="abs f-address">48 Tallow Road,<br>Wenmore Park WA 6099</div>
  <h4 class="abs f-head" style="left:650px;top:1082px">Newsletter</h4>
  <div class="abs email-input">Email address</div>
  <div class="abs join-btn">JOIN</div>
</footer>

</body>
</html>
```